Bravo K's Auto Detailing new business cards

I am a business owner who professionally details cars. I clean and detail the interiors, exteriors of vehicles. I need a logo designed for my new business Bravo K's Auto Detailing and a great designed card that will wow anyone that I hand it out to. Attached is a photo that I would like on side of the card. I want the picture to be on the right side of the card, while my busines name will be on the other side. I want the picture to have a slant where it divided the card into left and right, not just straight down. The picture will be printed glossy and I want the left half to have a carbon fiber background. Feel free to design a cool font for the business name, The business name needs to be a red gloss to pop out against the matte background. The back of the card should have my name Milo Fenwick. Under my name should be Owner/ Operator. then all my contact info and fb and instagram stuff. must include services offered- Paint Correction, Exterior detailing
Interior Detailing, Engine Bay Detailing, Headlight restoration, Ceramic Coatings

Target Market(s)

My target market is anyone who drives a vehicle.

Industry/Entity Type

Automotive

Contact Information for Business Card

Business name- Bravo K's Auto Detailing
Milo Fenwick Owner/ Operator
Location- Larkmoor, CA
Business # (559) 604-2179
email- milo@thebrightpolisher.example
fb and instragram logos- @thebrightpolisher

Font styles to use
Serif
Script
Other font styles liked:
• Blacksword

Colors
ec1f27
000000

Requirements
Must have
• The card must be in landscape position. All the details that are in the brief description which are my business name, my name, services offered and any other info thats in the project description. I uploaded pics of veltranos that I would like to see different designs incorporated into the backside of the card. File 5,6,and 7 are ideas that I would like to see done with my business name. The diamond around my name with the polisher coming around the bottom, and a Veltrano outline on the left side of the diamond kinda like file 5
• Also, business name and name should be in some style of script, while the rest of the fonts in serif. Must have the picture of me on the front right side of the card!!!
Nice to have
• Your own personal ideas that you think I am missing.
Should not have
• No grafitti, no generic logos around the business name like every other auto detail card on google.

```html
<!DOCTYPE html>
<html lang="en">
<head>
<meta charset="utf-8">
<title>Bravo K's Auto Detailing – Business Cards</title>
<link rel="stylesheet" href="https://fonts.googleapis.com/css2?family=Roboto:wght@400;500;700&family=Roboto+Condensed:wght@700&display=swap">
<style>
  :root {
    --page-bg: #e4e4e4;
    --card-bg: #151515;
    --card-bg-edge: #0d0d0d;
    --brand-red: #ec1f27;
    --deep-red: #c4161c;
    --text-light: #e2e2e2;
    --text-muted: #cfcfcf;
    --photo-dark: #0f1a2c;
    --photo-mid: #2a3f63;
    --photo-light: #8ea3c4;
  }
  html, body {
    margin: 0;
    width: 1200px;
    height: 960px;
    overflow: hidden;
    background: var(--page-bg);
    font-family: "Roboto", Arial, sans-serif;
  }
  .canvas { position: relative; width: 1200px; height: 960px; }

  .card {
    position: absolute;
    width: 601px;
    height: 343px;
    border-radius: 18px;
    overflow: hidden;
    background: linear-gradient(135deg, var(--card-bg) 0%, var(--card-bg-edge) 100%);
  }
  .card--front { left: 302px; top: 124px; }
  .card--back  { left: 299px; top: 493px; }

  .card-art { position: absolute; inset: 0; }

  /* Front */
  .brand {
    position: absolute;
    left: 50px;
    top: 52px;
    margin: 0;
    color: var(--brand-red);
    font-weight: 700;
    line-height: 1;
  }
  .brand-name {
    display: block;
    font-size: 35px;
    letter-spacing: 4px;
    text-transform: uppercase;
  }
  .brand-line {
    display: block;
    margin-top: 11px;
    font-size: 17px;
    letter-spacing: 12.5px;
    text-transform: uppercase;
  }
  .services { position: absolute; left: 49px; top: 146px; }
  .services-title {
    margin: 0 0 5px;
    color: var(--deep-red);
    font-size: 15px;
    font-weight: 500;
    text-transform: uppercase;
  }
  .services-list { list-style: none; margin: 0; padding: 0; }
  .services-list li {
    position: relative;
    padding-left: 15px;
    color: var(--text-muted);
    font-size: 14px;
    line-height: 20px;
  }
  .services-list li::before {
    content: "";
    position: absolute;
    left: 2px;
    top: 7px;
    width: 5px;
    height: 5px;
    border-radius: 50%;
    background: var(--deep-red);
  }

  /* Back */
  .contact {
    position: absolute;
    right: 29px;
    top: 158px;
    text-align: right;
  }
  .owner-name {
    margin: 0;
    color: var(--deep-red);
    font-family: "Roboto Condensed", "Arial Narrow", sans-serif;
    font-size: 23px;
    font-weight: 700;
    text-transform: uppercase;
    letter-spacing: 0.3px;
  }
  .owner-role {
    margin: 2px 0 0;
    padding-right: 3px;
    color: var(--text-light);
    font-size: 15px;
    font-weight: 500;
    text-transform: uppercase;
  }
  .contact-list { list-style: none; margin: 14px 0 0; padding: 0; }
  .contact-list li {
    display: flex;
    justify-content: flex-end;
    align-items: center;
    gap: 8px;
    color: var(--text-light);
    font-size: 14.5px;
    line-height: 20.5px;
  }
  .contact-icon { width: 14px; height: 14px; fill: var(--brand-red); }
  .social {
    display: flex;
    justify-content: flex-end;
    align-items: center;
    gap: 6px;
    margin-top: 12px;
    color: var(--text-light);
    font-size: 14.5px;
  }
  .social-mark {
    width: 16px;
    height: 16px;
    border-radius: 3px;
    background: #8a8f99;
  }
</style>
</head>
<body>
<main class="canvas">

  <section class="card card--front">
    <svg class="card-art" width="601" height="343" viewBox="0 0 601 343">
      <defs>
        <linearGradient id="portraitTone" x1="0" y1="0" x2="1" y2="1">
          <stop offset="0" stop-color="var(--photo-mid)"/>
          <stop offset="0.45" stop-color="var(--photo-dark)"/>
          <stop offset="1" stop-color="var(--photo-light)"/>
        </linearGradient>
      </defs>
      <polygon role="img" aria-label="Photo of the owner polishing a glossy black car bonnet with an orange-padded machine polisher"
               points="446,0 601,0 601,343 358,343" fill="url(#portraitTone)"/>
    </svg>

    <h1 class="brand">
      <span class="brand-name">Bravo K's</span>
      <span class="brand-line">Auto Detailing</span>
    </h1>

    <div class="services">
      <h2 class="services-title">Services Offered</h2>
      <ul class="services-list">
        <li>Paint Correction</li>
        <li>Exterior detailing</li>
        <li>Interior Detailing</li>
        <li>Engine Bay Detailing</li>
        <li>Headlight restoration</li>
        <li>Ceramic Coatings</li>
      </ul>
    </div>
  </section>

  <section class="card card--back">
    <svg class="card-art" width="600" height="343" viewBox="0 0 600 343">
      <defs>
        <radialGradient id="carTone" cx="0.4" cy="0.45" r="0.65">
          <stop offset="0" stop-color="#3a3d42"/>
          <stop offset="0.6" stop-color="#1c1d20"/>
          <stop offset="1" stop-color="#151515" stop-opacity="0"/>
        </radialGradient>
      </defs>
      <rect role="img" aria-label="Photo of a glossy black Veltrano supercar seen from the front three-quarter view"
            x="0" y="0" width="390" height="343" fill="url(#carTone)"/>
    </svg>

    <div class="contact">
      <h2 class="owner-name">Milo Fenwick</h2>
      <p class="owner-role">Owner/ Operator</p>
      <ul class="contact-list">
        <li>Larkmoor, CA
          <svg class="contact-icon" viewBox="0 0 14 14" aria-hidden="true"><path d="M7 0.5a4.6 4.6 0 0 0-4.6 4.6C2.4 8.6 7 13.5 7 13.5s4.6-4.9 4.6-8.4A4.6 4.6 0 0 0 7 0.5zm0 6.4a1.8 1.8 0 1 1 0-3.6 1.8 1.8 0 0 1 0 3.6z"/></svg>
        </li>
        <li>(559) 604-2179
          <svg class="contact-icon" viewBox="0 0 14 14" aria-hidden="true"><path d="M3 1l2.2 2.6-1.1 1.7c.8 1.7 2.1 3 3.8 3.8l1.7-1.1L12.2 10.2 11 12.6C6.1 12.3 1.7 7.9 1.4 3z"/></svg>
        </li>
        <li>milo@thebrightpolisher.example
          <svg class="contact-icon" viewBox="0 0 14 14" aria-hidden="true"><path d="M1 3.5h12v8H1z"/><path d="M1.5 4l5.5 4 5.5-4" fill="none" stroke="#151515" stroke-width="1.2"/></svg>
        </li>
      </ul>
      <div class="social">
        <span class="social-mark" aria-hidden="true"></span>
        <span>@thebrightpolisher</span>
      </div>
    </div>
  </section>

</main>
</body>
</html>
```